Bref créative
Stationary for telecom company
KLV Telecommunications
Professional
Dinh Quoc Bao
Director
47 Hoa Lu Street, Ward 5, Go Vap District, Ho Chi Minh City
bao.dinh@mrq.net.vn
www.klvtelecom.vn

```html
<!DOCTYPE html>
<html lang="en">
<head>
<meta charset="utf-8">
<title>KLV Telecommunications – Business Card</title>
<link rel="stylesheet" href="https://fonts.googleapis.com/css2?family=Open+Sans:wght@400;600;800&display=swap">
<style>
  :root {
    --bg: #e9ebee;
    --card: #ffffff;
    --brand-blue: #2c5b9c;
    --brand-blue-light: #6f93c4;
    --text-grey: #6a6f76;
    --shadow: rgba(40, 50, 70, 0.18);
  }
  * { box-sizing: border-box; margin: 0; padding: 0; }
  html, body {
    width: 1200px; height: 980px; overflow: hidden;
    background: var(--bg);
    font-family: "Open Sans", Arial, sans-serif;
  }
  .canvas { position: relative; width: 1200px; height: 980px; }
  .card {
    position: absolute; left: 210px;
    width: 780px; height: 446px;
    background: var(--card);
    border-radius: 26px;
    box-shadow: 0 10px 26px var(--shadow);
    overflow: hidden;
  }
  .card--front { top: 28px; }
  .card--back { top: 506px; }

  .brand-name {
    color: var(--brand-blue);
    font-weight: 800;
    line-height: 1;
    letter-spacing: 0.5px;
  }
  .card--front .brand-name {
    position: absolute; left: 52px; top: 46px;
    font-size: 34px;
  }
  .contact-list {
    position: absolute; left: 52px; top: 116px;
    list-style: none;
  }
  .contact-item {
    display: flex; align-items: center; gap: 12px;
    font-size: 14px; color: var(--text-grey);
    height: 26px;
  }
  .contact-item--continued { padding-left: 30px; }
  .contact-icon { width: 18px; height: 18px; flex: none; }
  .swoosh { position: absolute; inset: 0; }
  .person {
    position: absolute; right: 250px; top: 340px;
    text-align: right;
  }
  .person-name { color: var(--brand-blue); font-size: 22px; font-weight: 600; line-height: 1.2; }
  .person-title { color: var(--text-grey); font-size: 16px; margin-top: 4px; }

  .card--back .brand-name {
    position: absolute; left: 0; right: 0; top: 160px;
    text-align: center; font-size: 44px;
  }
  .website {
    position: absolute; left: 0; right: 0; top: 238px;
    text-align: center;
    font-size: 15px; letter-spacing: 9px;
    color: var(--text-grey);
  }
</style>
</head>
<body>
<main class="canvas">

  <section class="card card--front" aria-label="Business card front">
    <svg class="swoosh" viewBox="0 0 780 446" aria-hidden="true">
      <path d="M470 446 C 610 400, 720 270, 780 120 L 780 446 Z" fill="var(--brand-blue)"/>
      <path d="M520 446 C 650 405, 745 300, 780 210 L 780 446 Z" fill="#ffffff"/>
      <path d="M560 446 C 670 410, 752 330, 780 270 L 780 446 Z" fill="var(--brand-blue)"/>
      <path d="M430 446 C 590 390, 705 250, 755 40" fill="none" stroke="var(--brand-blue-light)" stroke-width="5"/>
    </svg>

    <div class="brand-name">KLV Telecommunications</div>

    <ul class="contact-list">
      <li class="contact-item">
        <svg class="contact-icon" viewBox="0 0 18 18" aria-hidden="true"><circle cx="9" cy="9" r="9" fill="var(--brand-blue)"/><path d="M9 4a3 3 0 0 1 3 3c0 2.2-3 6-3 6s-3-3.8-3-6a3 3 0 0 1 3-3z" fill="#fff"/></svg>
        47 Hoa Lu Street, Ward 5, Go Vap District
      </li>
      <li class="contact-item contact-item--continued">Ho Chi Minh City</li>
      <li class="contact-item">
        <svg class="contact-icon" viewBox="0 0 18 18" aria-hidden="true"><circle cx="9" cy="9" r="9" fill="var(--brand-blue)"/><path d="M6 4.5l2 2-1 1.2a6 6 0 0 0 3.3 3.3l1.2-1 2 2-1.3 1.5C8.6 13.2 4.8 9.4 4.5 5.8z" fill="#fff"/></svg>
        (84) 8 36 204 718
      </li>
      <li class="contact-item">
        <svg class="contact-icon" viewBox="0 0 18 18" aria-hidden="true"><circle cx="9" cy="9" r="9" fill="var(--brand-blue)"/><rect x="5" y="5.5" width="8" height="7" rx="1" fill="#fff"/></svg>
        (84) 8 36 204 719
      </li>
      <li class="contact-item">
        <svg class="contact-icon" viewBox="0 0 18 18" aria-hidden="true"><circle cx="9" cy="9" r="9" fill="var(--brand-blue)"/><rect x="4.5" y="5.5" width="9" height="7" fill="#fff"/><path d="M4.5 5.5L9 9.5l4.5-4" fill="none" stroke="var(--brand-blue)" stroke-width="1"/></svg>
        bao.dinh@mrq.net.vn
      </li>
      <li class="contact-item">
        <svg class="contact-icon" viewBox="0 0 18 18" aria-hidden="true"><circle cx="9" cy="9" r="9" fill="var(--brand-blue)"/><circle cx="9" cy="9" r="4.5" fill="none" stroke="#fff" stroke-width="1.4"/><path d="M4.5 9h9" stroke="#fff" stroke-width="1.2"/></svg>
        www.klvtelecom.vn
      </li>
    </ul>

    <div class="person">
      <div class="person-name">Dinh Quoc Bao</div>
      <div class="person-title">Director</div>
    </div>
  </section>

  <section class="card card--back" aria-label="Business card back">
    <div class="brand-name">KLV Telecommunications</div>
    <div class="website">www.klvtelecom.vn</div>
  </section>

</main>
</body>
</html>
```